continued... Web Design for Professional Development and marketplace

in addition to the homepages that you are desiging, can you also create designs for the attached wireframes that are part of the same website.
I am creating this as a seperate project as we are keen to see your designs for the rest of the website.
VIdeo of prototype and homepage designs
https://www.quellbin.net/sh/rk8tp2mqvx41hwa/7Gt3oLnQ2z/design
Updates
added an additional wireframe that was missed in the original upload
added one more wireframe for the homepage: where the user is prompted to login or signup
Industry/Entity Type
Marketplace
Look and feel
Each slider illustrates characteristics of the customer's brand and the style your logo design should communicate.

```html
<!DOCTYPE html>
<html lang="en">
<head>
<meta charset="utf-8">
<title>Professional Development Marketplace</title>
<link rel="stylesheet" href="https://fonts.googleapis.com/css2?family=Open+Sans:wght@400;600;700&family=Roboto:wght@400;500;700;900&display=swap">
<style>
:root{
  --page:#f2f2f2;
  --dark:#3b3b3b;
  --green:#3a9a6c;
  --green-light:#4fb584;
  --green-pale:#e4f3ea;
  --subnav:#e1efe7;
  --ink:#222;
  --muted:#555;
  --link:#1a1aff;
  --grey-star:#7b7f80;
  --white:#fff;
}
*{box-sizing:border-box;margin:0;padding:0}
html,body{width:1200px;height:844px;overflow:hidden;background:var(--page);font-family:"Roboto",Arial,sans-serif;color:var(--ink)}
.canvas{position:relative;width:1200px;height:844px}
.abs{position:absolute}
.page-bg{left:246px;top:26px;width:700px;height:410px;background:var(--white)}

/* header */
.topbar{left:246px;top:26px;width:700px;height:51px;background:var(--dark)}
.menu-btn{left:256px;top:35px;width:34px;height:34px;background:var(--green);display:flex;align-items:center;justify-content:center}
.search{left:298px;top:35px;width:164px;height:34px;background:var(--white);display:flex;align-items:center;justify-content:space-between;padding:0 6px 0 14px;font-size:12px}
.brand{left:480px;top:30px;width:150px;text-align:center;color:var(--white);font-family:"Open Sans",sans-serif;line-height:1}
.brand .big{font-size:25px;display:block}
.brand .small{font-size:11.5px;display:block;margin-top:1px}
.add-review-btn{left:649px;top:35px;width:81px;height:34px;background:var(--white);display:flex;align-items:center;gap:7px;padding-left:8px;font-size:11.5px;line-height:1.1}
.login-btn{left:752px;top:35px;width:82px;height:34px;background:var(--green);color:var(--white);display:flex;align-items:center;gap:7px;padding-left:9px;font-size:12px}
.signup-btn{left:855px;top:35px;width:82px;height:34px;background:var(--white);display:flex;align-items:center;justify-content:center;font-size:12px}

.subnav{left:246px;top:77px;width:700px;height:26px;background:var(--subnav);font-size:10px;font-weight:700;color:#444;font-family:"Open Sans",sans-serif}
.subnav span{position:absolute;top:6px}

.filters{left:246px;top:103px;width:700px;height:51px;display:flex;overflow:hidden}
.filter{height:51px;color:var(--white);text-align:center;padding-top:11px;font-size:12px;line-height:1.05;background:var(--green)}
.filter.alt{background:var(--green-light)}
.filter small{display:block;font-size:8.5px;opacity:.85;margin-top:1px}
.filter .caret{display:block;font-size:7px;height:7px}

.headline{left:304px;top:166px;font-size:26.5px;font-weight:900;line-height:27px;color:#000;letter-spacing:-.3px;white-space:nowrap;width:450px;overflow:hidden}
.learn{left:556px;top:221px;font-size:15px;color:var(--link)}
.cats{font-size:15.5px;color:#333;letter-spacing:-.2px}

/* dropdown */
.account{left:752px;top:70px;width:239px;height:192px;background:var(--white);border:1px solid var(--green)}
.account ul{list-style:none;position:absolute;left:12px;top:8px;font-size:11.5px;color:#444;line-height:20px}
.account .photo{position:absolute;left:116px;top:11px;width:109px;height:108px;background:linear-gradient(160deg,#6b7c8c,#3c4b5a 60%,#1e2630)}
.account .note{position:absolute;left:12px;top:146px;font-size:12px;color:#444;line-height:16px}
.account .note a{color:var(--link)}

/* sort */
.sortbar{left:246px;top:386px;width:700px;height:50px;background:var(--dark)}
.sort-label{left:264px;top:403px;color:var(--white);font-size:13px}
.sort-input{left:302px;top:394px;width:184px;height:33px;background:var(--white);border:1px solid #ccc;font-size:13px;padding:9px 9px;color:#444;font-family:"Open Sans",sans-serif}
.view-btn{top:394px;height:33px;background:var(--green);color:var(--white);display:flex;align-items:center;gap:15px;padding-left:8px;font-size:13px}

.review-band{left:246px;top:450px;width:700px;height:52px;background:var(--green);color:var(--white);display:flex;align-items:center;gap:12px;padding-left:22px;font-size:18px;font-weight:700;box-shadow:0 8px 10px -6px rgba(0,0,0,.45)}

/* cards */
.card{left:246px;width:700px;height:115px;border:1px solid var(--green);background:var(--white)}
.card.tint{background:var(--green-pale)}
.card > *{position:absolute}
.stars{left:27px;top:18px;display:flex;gap:3px}
.dates{left:32px;top:52px;font-size:9.6px;line-height:12.5px;color:#333}
.dates a{color:var(--link);text-decoration:none}
.price{left:32px;top:78px;font-size:14.5px;color:#333}
.course-title{left:199px;top:36px;font-size:18px;font-weight:700;color:var(--green);line-height:22px;font-family:"Open Sans",sans-serif}
.mode{left:418px;font-size:9.5px;color:#444;display:flex;align-items:center;gap:8px}
.provider{left:510px;top:25px;width:110px;text-align:center}
.provider .mark{display:flex;align-items:center;justify-content:center;gap:6px;font-size:12px;font-weight:700;color:var(--ink);height:30px}
.provider .mark i{display:block;width:14px;height:20px;background:var(--green)}
.provider .name{font-size:9.6px;color:#444;line-height:12px;margin-top:13px}
.fav{left:620px;top:20px;width:80px;text-align:center;font-size:9.6px;color:#444;line-height:12px}
</style>
</head>
<body>
<div class="canvas">
  <div class="abs page-bg"></div>

  <header class="abs topbar"></header>
  <div class="abs menu-btn"><svg width="24" height="20" viewBox="0 0 24 20"><g fill="#fff"><rect y="1" width="24" height="2"/><rect y="6" width="24" height="2"/><rect y="11" width="24" height="2"/><rect y="16" width="24" height="2"/></g></svg></div>
  <div class="abs search">Search<svg width="22" height="22" viewBox="0 0 22 22"><circle cx="9" cy="9" r="7" fill="none" stroke="#111" stroke-width="2.4"/><line x1="14" y1="14" x2="20" y2="20" stroke="#111" stroke-width="2.8"/></svg></div>
  <div class="abs brand"><span class="big">Professional</span><span class="small">Development Marketplace</span></div>
  <div class="abs add-review-btn"><svg width="16" height="16" viewBox="0 0 16 16"><path d="M6 0h4v6h6v4h-6v6H6v-6H0V6h6z" fill="#333"/></svg><span>Add<br>Review</span></div>
  <div class="abs login-btn"><svg width="14" height="16" viewBox="0 0 14 16"><circle cx="7" cy="4.5" r="4" fill="#fff"/><path d="M0 16c0-5 3-7 7-7s7 2 7 7z" fill="#fff"/></svg>Login</div>
  <div class="abs signup-btn">Sign up</div>

  <nav class="abs subnav"><span style="left:219px">About</span><span style="left:276px">Business</span><span style="left:348px">Developers</span></nav>

  <div class="abs filters">
    <div class="filter" style="width:72px">Save<span style="display:block;font-size:17px;margin-top:2px">+</span></div>
    <div class="filter alt" style="width:75px">Career<span class="caret">▼</span><small>(all)</small></div>
    <div class="filter alt" style="width:109px">Specialization<span class="caret">▼</span><small>(all)</small></div>
    <div class="filter" style="width:74px">Location<span class="caret">▼</span><small>(Vancouver)</small></div>
    <div class="filter alt" style="width:69px">Price<span class="caret">▼</span><small>($600-3000)</small></div>
    <div class="filter" style="width:93px">Start Date<span class="caret">▼</span><small>(2 - 6 months)</small></div>
    <div class="filter alt" style="width:208px;text-align:left;padding-left:4px"><span style="visibility:hidden">x</span><span class="caret"></span><small>(int</small></div>
  </div>

  <h1 class="abs headline">SELECT FROM THE CATEGORIES BELOW<br>THE BEST TRAINING TO ADVANCE YOUR</h1>
  <a class="abs learn">Learn More...</a>

  <div class="cats">
    <span class="abs" style="left:272px;top:260px">Design</span>
    <span class="abs" style="left:272px;top:288px">Medicine</span>
    <span class="abs" style="left:272px;top:317px">Marketing</span>
    <span class="abs" style="left:272px;top:345px">Product Management</span>
    <span class="abs" style="left:465px;top:260px">Software Development</span>
    <span class="abs" style="left:465px;top:288px">Project Management</span>
    <span class="abs" style="left:465px;top:317px">Business</span>
    <span class="abs" style="left:465px;top:345px">Sales</span>
    <span class="abs" style="left:661px;top:260px">...blah...</span>
    <span class="abs" style="left:661px;top:288px">...blah...</span>
    <span class="abs" style="left:661px;top:317px">...blah...</span>
    <span class="abs" style="left:661px;top:345px">...blah...</span>
    <span class="abs" style="left:790px;top:260px">...blah...</span>
    <span class="abs" style="left:790px;top:288px">...blah...</span>
    <span class="abs" style="left:790px;top:317px">New and Featured</span>
    <span class="abs" style="left:790px;top:345px">All</span>
  </div>

  <div class="abs account">
    <ul><li>Login</li><li>Favorites</li><li>Help</li><li>Evaluator</li><li>Profile</li><li>Logout Terms</li></ul>
    <div class="photo" role="img" aria-label="Profile photo of the signed-in member"></div>
    <p class="note">You have <a href="#">3 courses</a> that are<br>Starting in the next month</p>
  </div>

  <div class="abs sortbar"></div>
  <span class="abs sort-label">Sort</span>
  <div class="abs sort-input">Trending</div>
  <div class="abs view-btn" style="left:762px;width:83px"><svg width="18" height="18" viewBox="0 0 18 18" fill="#fff"><rect width="8" height="8"/><rect x="10" width="8" height="8"/><rect y="10" width="8" height="8"/><rect x="10" y="10" width="8" height="8"/></svg>Grid</div>
  <div class="abs view-btn" style="left:854px;width:83px"><svg width="24" height="18" viewBox="0 0 24 18" fill="#fff"><rect width="24" height="2"/><rect y="5" width="24" height="2"/><rect y="10" width="24" height="2"/><rect y="15" width="24" height="2"/></svg>List</div>

  <div class="abs review-band"><svg width="36" height="36" viewBox="0 0 36 36"><circle cx="18" cy="18" r="16" fill="none" stroke="#fff" stroke-width="3"/><path d="M16 9h4v7h7v4h-7v7h-4v-7H9v-4h7z" fill="#fff"/></svg>Add Review</div>

  <svg width="0" height="0" style="position:absolute"><defs>
    <path id="star" d="M11 0l3.4 7 7.6 1-5.5 5.3 1.3 7.6L11 17.3 4.2 20.9l1.3-7.6L0 8l7.6-1z"/>
    <g id="heart-ico"><path d="M26 44C10 32 3 24 3 15 3 8 8 3 14 3c5 0 9 3 12 7 3-4 7-7 12-7 6 0 11 5 11 12 0 9-7 17-23 29z" fill="none" stroke="#3a9a6c" stroke-width="3.4"/><path d="M9 13c0-3 2-5 5-5" fill="none" stroke="#3a9a6c" stroke-width="1.5"/></g>
  </defs></svg>

  <article class="abs card" style="top:516px">
    <div class="stars"><svg width="22" height="21"><use href="#star" fill="#3a9a6c"/></svg><svg width="22" height="21"><use href="#star" fill="#3a9a6c"/></svg><svg width="22" height="21"><use href="#star" fill="#3a9a6c"/></svg><svg width="22" height="21"><use href="#star" fill="#3a9a6c"/></svg><svg width="22" height="21"><use href="#star" fill="#7b7f80"/></svg></div>
    <p class="dates">2 / Sep / to 14 / Sep <a href="#">( and more )</a><br>Vancouver <a href="#">( and more )</a></p>
    <p class="price">$955</p>
    <h2 class="course-title">Product Management<br>Foundations</h2>
    <div class="mode" style="top:36px"><svg width="16" height="17" viewBox="0 0 14 16"><circle cx="7" cy="4.5" r="4" fill="#3a9a6c"/><path d="M0 16c0-5 3-7 7-7s7 2 7 7z" fill="#3a9a6c"/></svg>in - person</div>
    <div class="mode" style="top:61px"><svg width="20" height="17" viewBox="0 0 20 17"><rect x="1" y="1" width="18" height="11" fill="none" stroke="#3a9a6c" stroke-width="2"/><rect x="6" y="14" width="8" height="2" fill="#3a9a6c"/></svg>online</div>
    <div class="provider"><div class="mark"><i></i>HARBOURLINE</div><p class="name">Harbourline School of<br>Business</p></div>
    <div class="fav"><svg width="52" height="48" viewBox="0 0 52 48"><use href="#heart-ico"/></svg><p>Add to<br>Favorites</p></div>
  </article>

  <article class="abs card tint" style="top:645px">
    <div class="stars"><svg width="22" height="21"><use href="#star" fill="#3a9a6c"/></svg><svg width="22" height="21"><use href="#star" fill="#3a9a6c"/></svg><svg width="22" height="21"><use href="#star" fill="#3a9a6c"/></svg><svg width="22" height="21"><use href="#star" fill="#3a9a6c"/></svg><svg width="22" height="21"><use href="#star" fill="#7b7f80"/></svg></div>
    <p class="dates">2 / Sep / to 14 / Sep <a href="#">( and more )</a><br>Vancouver <a href="#">( and more )</a></p>
    <p class="price">$3995</p>
    <h2 class="course-title">Product Management<br>Foundations</h2>
    <div class="mode" style="top:36px"><svg width="16" height="17" viewBox="0 0 14 16"><circle cx="7" cy="4.5" r="4" fill="#3a9a6c"/><path d="M0 16c0-5 3-7 7-7s7 2 7 7z" fill="#3a9a6c"/></svg>in - person</div>
    <div class="mode" style="top:61px"><svg width="20" height="17" viewBox="0 0 20 17"><rect x="1" y="1" width="18" height="11" fill="none" stroke="#3a9a6c" stroke-width="2"/><rect x="6" y="14" width="8" height="2" fill="#3a9a6c"/></svg>online</div>
    <div class="provider"><div class="mark"><i></i>HARBOURLINE</div><p class="name">Harbourline School of<br>Business</p></div>
    <div class="fav"><svg width="52" height="48" viewBox="0 0 52 48"><use href="#heart-ico"/></svg><p>Add to<br>Favorites</p></div>
  </article>
</div>
</body>
</html>
```